Beautiful e-comm site for 'roadside farmers stand' online!

Need a logo design and basic e-comm website (super super simple) for new business called Brambletoft. Brambletoft is an online farmers stand where local artisans can sell 'brambletoft' goods directly from their makers!

Looking for something simple, whimsicle and clean! (Ideally with a light grey or perrywinkle and some color mixed in - word 'Brambletoft' in black - can work the pear shape in somewhere but not required!)

Target Market(s)

Hobby shoppers and 'quilo' goers who want a focus on edible things and care about ingredients!

Industry/Entity Type

E-Commerce

Number of Pages Required

2 page

Font styles to use
Decorative
Script

Colors
f3f1f8
ec1f27
cadf82

Requirements
Must have
• - Basic logo
• - Homepage
• - Product Detail Page
• - Be in a responsive, woocommerce or shopify, wordpress theme (will purchase theme after design is approved)
Nice to have
• - Matching check out & cart pages
• - 'About Us' page
• - SEO plugin
Should not have
• A cluttered look/feel.

```html
<!DOCTYPE html>
<html lang="en">
<head>
<meta charset="utf-8">
<title>Brambletoft — Online Farmers Stand</title>
<link rel="stylesheet" href="https://fonts.googleapis.com/css2?family=Open+Sans:wght@400;600;700&display=swap">
<style>
:root{
  --red:#e3101f;
  --green:#c3d970;
  --lavender:#efedf6;
  --ink:#222;
  --text:#444;
  --muted:#666;
  --line:#e2e2e2;
  --topbar:#f2f2f2;
  --black:#111;
  --footer:#1d1d1d;
  --footer-base:#141414;
  --white:#fff;
}
*{box-sizing:border-box;margin:0;padding:0}
html,body{width:1200px;height:2683px;overflow:hidden}
body{font-family:"Open Sans",Arial,sans-serif;color:var(--text);background:var(--white);position:relative}
a{color:inherit;text-decoration:none}
.abs{position:absolute}

/* top bar */
.topbar{left:0;top:0;width:1200px;height:54px;background:var(--topbar)}
.social{display:flex;gap:12px}
.social span{width:20px;height:20px;background:#333;border-radius:3px;display:block}
.topbar .social{position:absolute;left:80px;top:17px}
.toplinks{position:absolute;right:78px;top:18px;font-size:12px;font-weight:600;color:var(--red);display:flex;gap:10px}
.toplinks .free{margin-right:52px}

/* header */
.logo{left:72px;top:86px;font-size:41px;font-weight:700;color:var(--ink);letter-spacing:.3px}
.nav{left:384px;top:106px;display:flex;gap:0;font-size:13px;color:var(--ink)}
.nav a{position:absolute;white-space:nowrap}
.nav .active{color:var(--red)}

/* search */
.searchbar{left:75px;top:179px;width:1050px;height:64px;background:var(--black)}
.catselect{position:absolute;left:10px;top:10px;width:245px;height:44px;background:var(--white);font-size:12px;font-weight:600;color:var(--ink);padding:14px 14px}
.catselect svg{position:absolute;right:12px;top:16px}
.searchfield{position:absolute;left:265px;top:10px;width:575px;height:44px;background:var(--white);font-size:13px;color:#777;padding:13px 12px}
.searchfield svg{position:absolute;right:12px;top:12px}
.cart{position:absolute;left:870px;top:22px;font-size:13px;font-weight:600;color:var(--green);display:flex;gap:10px;align-items:center}

/* hero */
.hero{left:75px;top:260px;width:1050px;height:434px;background:linear-gradient(90deg,#5a5758 0%,#5f5a58 38%,#6b5040 55%,#5c3e2b 75%,#7a6a5c 100%)}
.hero h1{position:absolute;left:47px;top:100px;font-size:52px;font-weight:700;color:var(--white);letter-spacing:1px}
.hero p{position:absolute;left:51px;top:170px;width:520px;font-size:21px;font-weight:700;color:var(--white);line-height:31px}
.btn-red{background:var(--red);color:var(--white);font-weight:700;text-align:center}
.hero .btn-red{position:absolute;left:51px;top:255px;width:172px;height:48px;line-height:48px;font-size:19px}
.dots{position:absolute;left:53px;top:389px;display:flex;gap:11px}
.dots span{width:9px;height:9px;border-radius:50%;background:var(--white)}
.dots span:first-child{background:transparent;border:1.5px solid var(--white)}

/* tabs */
.rule{left:75px;top:746px;width:1050px;height:2px;background:var(--line)}
.tabs{left:0;top:772px;width:1200px;text-align:center;font-size:21px;font-weight:700;color:#777}
.tabs .on{color:var(--ink);text-decoration:underline;text-underline-offset:5px}
.tabs .sep{color:var(--ink);margin:0 24px}

/* products */
.card{width:241px;height:358px;border:1px solid var(--line);background:var(--white)}
.card .photo{position:absolute;left:20px;top:14px;width:200px;height:200px;border-radius:8px}
.card h3{position:absolute;left:0;top:212px;width:100%;text-align:center;font-size:15px;font-weight:400;color:var(--text);line-height:23px}
.card .price{position:absolute;left:0;top:265px;width:100%;text-align:center;font-size:15px;font-weight:700;color:var(--red)}
.card .add{position:absolute;left:54px;top:303px;width:132px;height:36px;line-height:36px;background:var(--green);color:var(--ink);font-size:13px;font-weight:700;text-align:center}

/* features */
.feature{width:330px;height:122px;border:3px solid #aaa;background:var(--white)}
.feature svg{position:absolute;left:38px;top:38px}
.feature h4{position:absolute;left:110px;top:22px;font-size:18px;font-weight:700;color:var(--ink)}
.feature p{position:absolute;left:110px;top:55px;width:200px;font-size:12.5px;line-height:19px;color:var(--text)}

/* about */
.about{left:0;top:1799px;width:1200px;height:318px;background:var(--lavender);text-align:center}
.about h2{position:absolute;left:0;top:40px;width:100%;font-size:27px;font-weight:700;color:var(--ink);letter-spacing:.5px}
.about p{position:absolute;left:80px;top:92px;width:1040px;font-size:15px;line-height:25px;color:var(--text)}
.about .btn-red{position:absolute;left:534px;top:222px;width:132px;height:37px;line-height:37px;font-size:14px}

/* newsletter + service */
.panel{top:2136px;width:512px;height:162px;background:var(--green);text-align:center}
.panel h3{position:absolute;left:0;width:100%;font-size:18px;font-weight:700;color:var(--ink);letter-spacing:.5px}
.newsletter h3{top:24px}
.newsletter .sub{position:absolute;left:0;top:58px;width:100%;font-size:13px;color:var(--ink)}
.emailbox{position:absolute;left:27px;top:90px;width:365px;height:49px;background:var(--white);text-align:left;font-size:12px;color:#555;padding:16px 0 0 48px}
.emailbox svg{position:absolute;left:14px;top:17px}
.newsletter .btn-red{position:absolute;left:392px;top:90px;width:92px;height:49px;line-height:49px;font-size:15px}
.service h3{top:34px}
.service .phone{position:absolute;left:0;top:68px;width:100%;font-size:23px;font-weight:700;color:var(--red)}
.service .phone svg{vertical-align:-2px;margin-right:10px}
.service .hours{position:absolute;left:0;top:111px;width:100%;font-size:13px;color:var(--ink)}

/* footer */
.footer{left:0;top:2343px;width:1200px;height:279px;background:var(--footer)}
.fcol{position:absolute;top:40px}
.fcol h5{font-size:14px;font-weight:700;color:var(--green);margin-bottom:10px;letter-spacing:.3px}
.fcol li{list-style:none;font-size:11.5px;color:#ddd;line-height:28px;text-transform:uppercase}
.fcol li svg{vertical-align:-2px;margin-right:8px}
.footer .social{position:absolute;left:829px;top:216px;gap:17px}
.footer .social span{width:28px;height:28px;background:#ccc}
.basebar{left:0;top:2622px;width:1200px;height:61px;background:var(--footer-base)}
.basebar .copy{position:absolute;left:75px;top:22px;font-size:11.5px;color:#aaa}
.cards{position:absolute;left:868px;top:17px;display:flex;gap:12px}
.cards span{width:40px;height:27px;background:#ddd;border-radius:4px;display:block}
</style>
</head>
<body>

<div class="abs topbar">
  <div class="social"><span></span><span></span><span></span><span></span><span></span><span></span></div>
  <div class="toplinks"><span class="free">FREE SHIPPING OVER $275</span><a href="#">REGISTER</a><span>|</span><a href="#">LOG IN</a><span>|</span><a href="#">MY ACCOUNT</a></div>
</div>

<div class="abs logo">Brambletoft</div>
<nav class="abs nav">
  <a class="active" style="left:0">HOME</a>
  <a style="left:101px">ABOUT</a>
  <a style="left:208px">PRODUCTS</a>
  <a style="left:342px">SHOP</a>
  <a style="left:438px">REVIEWS</a>
  <a style="left:559px">BLOG</a>
  <a style="left:655px">CONTACT US</a>
</nav>

<div class="abs searchbar">
  <div class="catselect">PRODUCT CATEGORIES
    <svg width="7" height="12" viewBox="0 0 7 12"><path d="M3.5 0L7 4.5H0zM3.5 12L0 7.5h7z" fill="#333"/></svg>
  </div>
  <div class="searchfield">Search keywords...
    <svg width="20" height="20" viewBox="0 0 20 20"><circle cx="8" cy="8" r="6" fill="none" stroke="#111" stroke-width="2.6"/><path d="M12.5 12.5L18 18" stroke="#111" stroke-width="3"/></svg>
  </div>
  <div class="cart">
    <svg width="20" height="18" viewBox="0 0 20 18"><path d="M0 1h4l3 10h10l2-7H6" fill="none" stroke="#fff" stroke-width="2"/><circle cx="8" cy="15" r="2" fill="#fff"/><circle cx="16" cy="15" r="2" fill="#fff"/></svg>
    <span>Shopping Cart &nbsp;(0)</span>
  </div>
</div>

<section class="abs hero" role="img" aria-label="Tray of freshly baked chocolate chip cookies on parchment">
  <h1>Brambletoft</h1>
  <p>Morbi condimentum suscipit odio, vitae consectetur mauris tempor vitae.</p>
  <a class="btn-red" href="#">Shop Now</a>
  <div class="dots"><span></span><span></span><span></span><span></span></div>
</section>

<div class="abs rule"></div>
<div class="abs tabs"><span class="on">FEATURED PRODUCTS</span><span class="sep">|</span><span>NEW ARRIVALS</span></div>

<div class="abs card" style="left:75px;top:838px"><div class="photo" role="img" aria-label="Salted caramel candies" style="background:radial-gradient(#d58a3a,#fff 70%)"></div><h3>Vestibulum ante ipsum<br>primis in faucibus</h3><div class="price">$27.99</div><a class="add">Add to Cart</a></div>
<div class="abs card" style="left:345px;top:838px"><div class="photo" role="img" aria-label="Jar of pickled cucumbers" style="background:radial-gradient(ellipse 30% 45%,#8a7a3a,#fff 90%)"></div><h3>Vestibulum ante ipsum<br>primis in faucibus</h3><div class="price">$27.99</div><a class="add">Add to Cart</a></div>
<div class="abs card" style="left:615px;top:838px"><div class="photo" role="img" aria-label="Handmade soap bars" style="background:radial-gradient(#e9dca0,#fff 72%)"></div><h3>Vestibulum ante ipsum<br>primis in faucibus</h3><div class="price">$27.99</div><a class="add">Add to Cart</a></div>
<div class="abs card" style="left:885px;top:838px"><div class="photo" role="img" aria-label="Jar of raspberry jam with fresh raspberries" style="background:radial-gradient(ellipse 30% 45%,#a5202e,#fff 90%)"></div><h3>Vestibulum ante ipsum<br>primis in faucibus</h3><div class="price">$27.99</div><a class="add">Add to Cart</a></div>

<div class="abs card" style="left:75px;top:1223px"><div class="photo" role="img" aria-label="Jar of berry jam with cloth lid" style="background:radial-gradient(ellipse 30% 45%,#9c1c2c,#fff 90%)"></div><h3>Vestibulum ante ipsum<br>primis in faucibus</h3><div class="price">$27.99</div><a class="add">Add to Cart</a></div>
<div class="abs card" style="left:345px;top:1223px"><div class="photo" role="img" aria-label="Red fruit jelly pieces" style="background:radial-gradient(ellipse 50% 30%,#e0283f,#fff 90%)"></div><h3>Vestibulum ante ipsum<br>primis in faucibus</h3><div class="price">$27.99</div><a class="add">Add to Cart</a></div>
<div class="abs card" style="left:615px;top:1223px"><div class="photo" role="img" aria-label="Chocolate chip cookies" style="background:radial-gradient(ellipse 50% 30%,#b9783e,#fff 90%)"></div><h3>Vestibulum ante ipsum<br>primis in faucibus</h3><div class="price">$27.99</div><a class="add">Add to Cart</a></div>
<div class="abs card" style="left:885px;top:1223px"><div class="photo" role="img" aria-label="Jar of pickles lying on its side" style="background:radial-gradient(ellipse 45% 35%,#8d8f42,#fff 90%)"></div><h3>Vestibulum ante ipsum<br>primis in faucibus</h3><div class="price">$27.99</div><a class="add">Add to Cart</a></div>

<div class="abs feature" style="left:75px;top:1630px">
  <svg width="46" height="34" viewBox="0 0 46 34"><path d="M0 4h28v20H0zM30 10h9l7 8v6H30z" fill="var(--red)"/><circle cx="9" cy="27" r="5" fill="var(--red)" stroke="#fff" stroke-width="2"/><circle cx="37" cy="27" r="5" fill="var(--red)" stroke="#fff" stroke-width="2"/></svg>
  <h4>Free Shipping</h4><p>Free Shipping on Orders Over $250, only within the U.S.</p>
</div>
<div class="abs feature" style="left:435px;top:1630px">
  <svg width="30" height="38" viewBox="0 0 30 38"><path d="M0 2h30v16c0 10-8 16-15 20C8 34 0 28 0 18z" fill="var(--red)"/><path d="M7 8h16v10c0 6-4 10-8 12C11 28 7 24 7 18z" fill="#fff"/></svg>
  <h4>Secure Shopping</h4><p>Your security and privacy is our highest concern.<br>Shop with trust.</p>
</div>
<div class="abs feature" style="left:796px;top:1630px">
  <svg width="28" height="38" viewBox="0 0 28 38"><path d="M14 0C6 0 0 6 0 14c0 10 14 24 14 24s14-14 14-24C28 6 22 0 14 0z" fill="var(--red)"/><circle cx="14" cy="14" r="5" fill="#fff"/></svg>
  <h4>Find Vendors</h4><p>Request a free sample of each of our products before you buy bulk.</p>
</div>

<section class="abs about">
  <h2>ABOUT OUR COMPANY</h2>
  <p>Aliquam molestie, mi et imperdiet euismod, dui purus auctor tellus, et interdum lacus lectus et ante. Sed accumsan sollicitudin sapien, sit amet adipiscing turpis gravida ac. In congue, neque ac lobortis volutpat, libero mauris varius mi, vitae suscipit ipsum ligula vitae risus. Duis aliquam nibh a dui iaculis viverra id a velit. Vivamus egestas risus in magna varius commodo. Sed semper viverra egestas.<br>Etiam pretium porttitor lectus, vel ornare neque porta volutpat.</p>
  <a class="btn-red" href="#">Read More</a>
</section>

<div class="abs panel newsletter" style="left:75px">
  <h3>NEWSLETTER SIGN UP</h3>
  <div class="sub">Subscribe to our newsletter for deals and coupons</div>
  <div class="emailbox"><svg width="20" height="14" viewBox="0 0 20 14"><rect width="20" height="14" rx="1" fill="#888"/><path d="M0 1l10 7 10-7" fill="none" stroke="#fff" stroke-width="1.5"/></svg>Enter Email Address</div>
  <a class="btn-red" href="#">Sign Up</a>
</div>
<div class="abs panel service" style="left:614px">
  <h3>CUSTOMER SERVICE</h3>
  <div class="phone"><svg width="18" height="18" viewBox="0 0 18 18"><path d="M4 0l4 4-2 3c1 2 3 4 5 5l3-2 4 4-3 4C8 18 0 10 0 3z" fill="var(--red)"/></svg>1-800-555-0142</div>
  <div class="hours">Monday through Friday 9am to 5pm PST</div>
</div>

<footer class="abs footer">
  <div class="fcol" style="left:75px"><h5>INFORMATION</h5><ul><li>About Us</li><li>Privacy Policy</li><li>Terms &amp; Conditions</li><li>Product Certifications</li><li>Product Guides</li><li>Contact Us</li><li>Blog</li></ul></div>
  <div class="fcol" style="left:350px"><h5>MY ACCOUNT</h5><ul><li>Account</li><li>Orders</li><li>Returns</li><li>Shipping</li><li>Rewards Program</li></ul></div>
  <div class="fcol" style="left:597px"><h5>SHOP</h5><ul><li>Product Index</li><li>Category Index</li><li>Business Samples</li><li>Coupons</li><li>Cart</li></ul></div>
  <div class="fcol" style="left:829px"><h5>CONTACT INFO</h5><ul>
    <li>4127 Hollowmere Lane</li><li>Ashford, KT 22081</li>
    <li><svg width="11" height="11" viewBox="0 0 18 18"><path d="M4 0l4 4-2 3c1 2 3 4 5 5l3-2 4 4-3 4C8 18 0 10 0 3z" fill="#ddd"/></svg>1-800-555-0142</li>
    <li><svg width="12" height="9" viewBox="0 0 20 14"><rect width="20" height="14" fill="#ddd"/><path d="M0 1l10 7 10-7" fill="none" stroke="#1d1d1d" stroke-width="1.5"/></svg>info@brambletoft.shop</li>
  </ul></div>
  <div class="social"><span></span><span></span><span></span><span></span><span></span><span></span></div>
</footer>

<div class="abs basebar">
  <div class="copy">Copyright © 2018 Brambletoft. All Right Reserved</div>
  <div class="cards"><span></span><span></span><span></span><span></span></div>
</div>

</body>
</html>
```